Complete Banner Set For Web Display Ads - Including Zimbly

Ads are driving to a free web class on real estate investing made easy. The offer is for software and training that solves their number 1 challenge - Finding Deals.
Examples of copy suggestions and offer....
"Invest In Real Estate Like A Pro"
"Access Never Before Seen Inventory In Seconds"
"The Country's Best Source For Off-Market Deals"
Brody Halvaney "#1 Real Estate Investing Strategy"
Real Estate

```html
<!DOCTYPE html>
<html lang="en">
<head>
<meta charset="utf-8">
<title>Brody Halvaney – Display Banner Set</title>
<link href="https://fonts.googleapis.com/css2?family=Open+Sans:wght@300;400;600;700;800&family=Oswald:wght@400;500;600&display=swap" rel="stylesheet">
<style>
:root{
  --orange:#f7941d;
  --orange-dark:#e9820f;
  --green:#6ea72d;
  --green-light:#8cc63f;
  --ink:#1e1e1e;
  --white:#ffffff;
  --paper:#ffffff;
}
*{box-sizing:border-box;margin:0;padding:0}
html,body{width:1200px;height:1200px;overflow:hidden;background:var(--paper)}
body{position:relative;font-family:"Open Sans",Arial,sans-serif}
.banner{position:absolute;width:292px;height:246px;overflow:hidden}
.abs{position:absolute}
.photo{position:absolute}
.cond{font-family:"Oswald","Arial Narrow",sans-serif}
.name{font-family:"Oswald","Arial Narrow",sans-serif;font-weight:500;color:var(--white);white-space:nowrap}
.btn-light{background:#f2f2f2;color:var(--ink);font-weight:700;font-size:13px;border-radius:4px;display:flex;align-items:center;justify-content:space-between;padding:0 10px}
.badge{position:absolute;width:62px;height:62px}
.badge span{position:absolute;inset:0;display:flex;flex-direction:column;align-items:center;justify-content:center;font-weight:700;font-size:11px;line-height:12px;color:var(--green-light);letter-spacing:1px}
.outline-btn{border:1px solid rgba(255,255,255,.85);border-radius:4px;color:var(--white);font-weight:600;font-size:11.5px;letter-spacing:1.5px;display:flex;align-items:center;justify-content:center}
.shadowtext{text-shadow:0 1px 3px rgba(0,0,0,.55)}
.tilt{transform:rotate(-12deg);transform-origin:left top;white-space:nowrap}

.b1{left:54px;top:46px}.b2{left:454px;top:46px}.b3{left:855px;top:46px}
.b4{left:54px;top:321px}.b5{left:454px;top:321px}.b6{left:855px;top:321px}
.b7{left:54px;top:609px}.b8{left:454px;top:609px}.b9{left:855px;top:609px}
.b10{left:454px;top:908px}
</style>
</head>
<body>

<section class="banner b1" style="background:var(--white)">
  <div class="abs" style="left:27px;top:0;width:264px;height:3px;background:var(--green)"></div>
  <div class="photo" role="img" aria-label="Investor in light grey blazer standing by a white porch" style="left:0;top:4px;width:118px;height:242px;background:linear-gradient(180deg,#e9ecef,#c9d0d6 55%,#8a939b)"></div>
  <div class="abs" style="left:114px;top:37px;width:139px;height:35px;background:var(--orange);color:#fff;font-weight:700;font-size:24px;line-height:35px;padding-left:10px">INVEST IN</div>
  <div class="abs" style="left:114px;top:79px;width:172px;height:38px;background:#f7a13a;color:#fff;font-weight:700;font-size:24px;line-height:38px;padding-left:10px">REAL ESTATE</div>
  <div class="abs" style="left:124px;top:128px;color:var(--green);font-weight:700;font-size:23px">LIKE A PRO...</div>
  <div class="abs" style="left:0;top:194px;width:292px;height:42px;background:var(--green)"></div>
  <div class="abs name" style="left:12px;top:202px;font-size:20px">Brody Halvaney</div>
  <div class="abs btn-light" style="left:165px;top:203px;width:114px;height:26px">Get Started <span>›</span></div>
</section>

<section class="banner b2">
  <div class="photo" role="img" aria-label="Investor seated on outdoor stairs" style="inset:0;background:linear-gradient(160deg,#6b5a48,#3a3029 50%,#1f1b18)"></div>
  <div class="abs" style="left:0;top:0;width:265px;height:3px;background:var(--orange)"></div>
  <div class="abs shadowtext" style="left:17px;top:112px;font-size:16.5px;color:var(--orange);white-space:nowrap">Invest In <b style="color:#fff">Real Estate</b> Like A Pro..</div>
  <div class="abs shadowtext" style="left:0;width:292px;top:148px;text-align:center;color:#fff;font-weight:700;font-size:12.5px;line-height:15px">The Country's Best Source For<br>Off-Market Deals</div>
  <div class="abs" style="left:0;top:194px;width:292px;height:42px;background:var(--green)"></div>
  <div class="abs name" style="left:12px;top:202px;font-size:20px">Brody Halvaney</div>
  <div class="abs btn-light" style="left:166px;top:203px;width:114px;height:26px">Get Started <span>›</span></div>
</section>

<section class="banner b3" style="background:var(--green)">
  <div class="photo" role="img" aria-label="Close portrait of investor in grey jacket" style="left:0;top:0;width:114px;height:246px;background:linear-gradient(180deg,#5a5550,#3b3835 60%,#2a2826)"></div>
  <div class="abs" style="left:114px;top:0;width:178px;height:246px;background:linear-gradient(180deg,#76b12f,#5f9a25)"></div>
  <div class="abs" style="left:124px;top:20px;width:130px;height:1px;background:#fff;opacity:.8"></div>
  <div class="abs name" style="left:124px;top:22px;font-size:21px;font-weight:400">Brody Halvaney</div>
  <div class="abs" style="left:124px;top:54px;width:130px;height:1px;background:#fff;opacity:.8"></div>
  <div class="abs cond" style="left:126px;top:72px;color:#fff;font-size:44px;font-weight:600;line-height:44px">#1</div>
  <div class="abs cond" style="left:126px;top:124px;color:#fff;font-size:20px;font-weight:500;line-height:26px">REAL ESTATE<br>INVESTING STRATEGY</div>
  <div class="abs" style="left:125px;top:191px;width:115px;height:28px;background:var(--ink);border-radius:4px;color:var(--orange);font-weight:700;font-size:13px;display:flex;align-items:center;justify-content:space-between;padding:0 10px">Get Started <span>›</span></div>
</section>

<section class="banner b4">
  <div class="photo" role="img" aria-label="Suburban street with houses in green tint" style="inset:0;background:linear-gradient(180deg,#7fb35a,#5e9b6f 55%,#4c8a74)"></div>
  <div class="photo" role="img" aria-label="Investor in light blazer standing" style="left:12px;top:40px;width:92px;height:206px;background:linear-gradient(180deg,#d9dee2,#b2bcc4 60%,#58636d)"></div>
  <div class="abs" style="left:0;width:292px;top:11px;text-align:center;color:#fff;font-size:16px;font-weight:300">Invest <b>In</b> Real Estate <b>Like A Pro</b></div>
  <div class="abs shadowtext" style="left:126px;width:130px;top:52px;text-align:center;color:#fff;font-size:15px;line-height:20px">
    <div style="font-weight:300">THE COUNTRY'S</div>
    <div style="font-weight:700">BEST SOURCE</div>
    <div style="display:inline-block;background:var(--ink);font-size:11px;line-height:14px;padding:0 4px;font-weight:700;text-shadow:none">For</div>
    <div style="font-weight:400">Off-Market Deals</div>
  </div>
  <div class="abs" style="left:126px;top:144px;width:114px;height:26px;background:var(--ink);border-radius:5px;color:var(--green-light);font-size:13px;letter-spacing:1px;display:flex;align-items:center;justify-content:center">GET STARTED</div>
  <svg class="abs" style="left:100px;top:190px" width="192" height="42" viewBox="0 0 192 42"><polygon points="0,42 22,0 192,0 192,42" fill="var(--orange)"/><polygon points="0,42 10,28 22,42" fill="var(--orange-dark)"/></svg>
  <div class="abs" style="right:14px;top:196px;color:#fff;font-size:20px;font-weight:300;white-space:nowrap">Brody Halvaney</div>
</section>

<section class="banner b5">
  <div class="photo" role="img" aria-label="Textured beige wall backdrop" style="inset:0;background:linear-gradient(135deg,#cfc3a8,#b9ad93)"></div>
  <div class="photo" role="img" aria-label="Smiling investor portrait" style="left:180px;top:16px;width:112px;height:200px;background:linear-gradient(180deg,#a48b72,#6f6a68 55%,#3e4650)"></div>
  <div class="abs" style="left:12px;top:13px;width:186px;height:27px;background:#fff;color:#333;font-size:18px;line-height:27px;padding-left:10px;white-space:nowrap">Invest <b>In</b> Real Estate</div>
  <div class="abs" style="left:12px;top:44px;width:119px;height:28px;background:var(--green);color:#fff;font-weight:700;font-size:19px;line-height:28px;padding-left:10px">Like A Pro</div>
  <div class="abs shadowtext" style="left:19px;top:91px;color:#fff;font-size:15px;line-height:19px">
    <div style="font-weight:300">THE COUNTRY'S</div><div style="font-weight:700">BEST SOURCE FOR</div><div>Off-Market Deals</div>
  </div>
  <svg class="abs" style="left:0;top:190px" width="292" height="56" viewBox="0 0 292 56"><path d="M0 0 C 60 30, 180 32, 292 20 L292 56 L0 56 Z" fill="var(--orange)"/></svg>
  <div class="abs" style="right:12px;top:217px;color:#fff;font-size:19px;font-weight:600;white-space:nowrap">Brody Halvaney</div>
  <div class="badge" style="left:0;top:167px"><svg width="62" height="62" viewBox="0 0 62 62"><polygon fill="#111" points="31,0 35,8 43,3 44,12 53,10 51,19 60,21 55,28 62,33 54,38 58,46 49,47 50,56 41,53 38,62 31,56 24,62 21,53 12,56 13,47 4,46 8,38 0,33 7,28 2,21 11,19 9,10 18,12 19,3 27,8"/></svg><span>CLICK<br>NOW</span></div>
</section>

<section class="banner b6">
  <div class="photo" role="img" aria-label="Suburban house exterior, muted tones" style="inset:0;background:linear-gradient(135deg,#8c8f86,#5f6658 60%,#4b5249)"></div>
  <div class="photo" role="img" aria-label="Investor portrait" style="left:180px;top:6px;width:112px;height:210px;background:linear-gradient(180deg,#a08770,#6a6767 55%,#3c444d)"></div>
  <div class="abs" style="left:12px;top:13px;width:186px;height:27px;background:#fff;color:#333;font-size:18px;line-height:27px;padding-left:10px;white-space:nowrap">Invest <b>In</b> Real Estate</div>
  <div class="abs" style="left:12px;top:44px;width:119px;height:28px;background:var(--green);color:#fff;font-weight:700;font-size:19px;line-height:28px;padding-left:10px">Like A Pro</div>
  <div class="abs shadowtext" style="left:19px;top:91px;color:#fff;font-size:15px;line-height:19px">
    <div style="font-weight:300">THE COUNTRY'S</div><div style="font-weight:700">BEST SOURCE FOR</div><div>Off-Market Deals</div>
  </div>
  <svg class="abs" style="left:0;top:190px" width="292" height="56" viewBox="0 0 292 56"><path d="M0 0 C 60 30, 180 32, 292 20 L292 56 L0 56 Z" fill="var(--orange)"/></svg>
  <div class="abs" style="right:12px;top:217px;color:#fff;font-size:19px;font-weight:600;white-space:nowrap">Brody Halvaney</div>
  <div class="badge" style="left:17px;top:167px"><svg width="62" height="62" viewBox="0 0 62 62"><polygon fill="#111" points="31,0 35,8 43,3 44,12 53,10 51,19 60,21 55,28 62,33 54,38 58,46 49,47 50,56 41,53 38,62 31,56 24,62 21,53 12,56 13,47 4,46 8,38 0,33 7,28 2,21 11,19 9,10 18,12 19,3 27,8"/></svg><span>CLICK<br>NOW</span></div>
</section>

<section class="banner b7">
  <div class="photo" role="img" aria-label="Faded house and street backdrop" style="inset:0;background:linear-gradient(180deg,#eceff1,#d6dbdf 60%,#b9bfc4)"></div>
  <div class="photo" role="img" aria-label="Investor in light blazer" style="left:30px;top:4px;width:94px;height:242px;background:linear-gradient(180deg,#d6dbe0,#aeb8c1 60%,#3d4f6a)"></div>
  <div class="abs tilt" style="left:130px;top:76px;font-size:21px;color:#222"><b>Brody</b> Halvaney</div>
  <div class="abs tilt" style="left:-10px;top:132px;width:330px;height:26px;background:var(--orange);color:#fff;font-size:16px;line-height:26px;padding-left:32px">Invest <b>In</b> Real Estate <b>Like A Pro</b></div>
  <div class="abs tilt" style="left:-5px;top:157px;width:330px;height:50px;background:var(--green-light);color:#fff;font-size:14px;line-height:19px;padding:6px 0 0 24px;text-align:center">
    <div style="width:270px">THE COUNTRY'S <b>BEST SOURCE FOR</b></div>
    <div style="width:270px">Off-Market Deals</div>
  </div>
  <div class="badge" style="left:226px;top:176px"><svg width="62" height="62" viewBox="0 0 62 62"><polygon fill="#111" points="31,0 35,8 43,3 44,12 53,10 51,19 60,21 55,28 62,33 54,38 58,46 49,47 50,56 41,53 38,62 31,56 24,62 21,53 12,56 13,47 4,46 8,38 0,33 7,28 2,21 11,19 9,10 18,12 19,3 27,8"/></svg><span>CLICK<br>NOW</span></div>
</section>

<section class="banner b8">
  <div class="abs" style="inset:0;background:linear-gradient(90deg,#a7bd3a,#c0a43a 70%,#d49a3a)"></div>
  <div class="photo" role="img" aria-label="Portrait of investor seated on stairs" style="left:196px;top:0;width:96px;height:246px;background:linear-gradient(180deg,#6a5a4c,#4a4a4e 55%,#2c3038)"></div>
  <div class="abs" style="left:176px;top:0;width:20px;height:246px;background:#d39a4e;opacity:.85"></div>
  <div class="abs" style="left:176px;top:6px;width:20px;text-align:center;color:#fff;opacity:.6;font-family:Oswald,sans-serif;font-size:14px;line-height:16px">B<br>R<br>O<br>D<br>Y<br><br>H<br>A<br>L<br>V<br>A<br>N<br>E<br>Y</div>
  <div class="abs name" style="left:28px;top:18px;font-size:22px;font-weight:400">Brody Halvaney</div>
  <div class="abs cond" style="left:31px;top:56px;color:#fff;font-size:46px;font-weight:600;line-height:48px">#1</div>
  <div class="abs cond" style="left:31px;top:114px;color:#fff;font-size:22px;font-weight:500;line-height:26px">REAL ESTATE<br>INVESTING<br>STRATEGY</div>
  <div class="abs outline-btn" style="left:31px;top:202px;width:102px;height:28px">CLICK NOW</div>
</section>

<section class="banner b9">
  <div class="photo" role="img" aria-label="Investor standing in front of a suburban house" style="inset:0;background:linear-gradient(180deg,#d7dde2,#aeb8c0 60%,#6e7c88)"></div>
  <svg class="abs" style="left:0;top:0" width="200" height="246" viewBox="0 0 200 246"><polygon points="0,0 128,0 195,123 140,246 0,246" fill="#fff"/><polygon points="0,0 122,0 187,123 133,246 0,246" fill="var(--orange)"/></svg>
  <div class="abs cond" style="left:25px;top:60px;color:#fff;font-size:46px;font-weight:600;line-height:48px">#1</div>
  <div class="abs cond" style="left:25px;top:106px;color:#fff;font-size:22px;font-weight:500;line-height:26px">REAL ESTATE<br>INVESTING<br>STRATEGY</div>
  <div class="abs outline-btn" style="left:26px;top:202px;width:102px;height:28px">CLICK NOW</div>
  <div class="abs" style="left:155px;top:191px;width:137px;height:43px;background:rgba(40,40,40,.88)"></div>
  <div class="abs name" style="right:9px;top:197px;font-size:21px;font-weight:400">Brody Halvaney</div>
</section>

<section class="banner b10" style="background:var(--orange)">
  <div class="abs cond" style="left:24px;top:20px;color:#fff;font-size:22.5px;font-weight:500;line-height:25.5px">THE<br>COUNTRY'S<br>BEST SOURCE<br>FOR OFF-MARKET<br>DEALS</div>
  <div class="abs" style="left:25px;top:164px;color:#fff;font-size:13px;line-height:16px">Invest In <b>Real Estate</b><br>Like A Pro</div>
  <div class="abs" style="left:24px;top:206px;color:var(--ink);font-size:12px;font-weight:700">GET STARTED NOW!</div>
  <div class="photo" role="img" aria-label="Investor seated on outdoor stairs" style="left:180px;top:6px;width:104px;height:105px;background:linear-gradient(180deg,#6a5a4c,#4b4644 55%,#2c3038)"></div>
  <div class="abs" style="left:180px;width:104px;top:116px;text-align:center;color:#333;font-size:12.5px;white-space:nowrap">Brody Halvaney</div>
  <div class="photo" role="img" aria-label="Large suburban house with driveway" style="left:188px;top:140px;width:90px;height:92px;background:linear-gradient(180deg,#cfe0ef,#b7c2a8 55%,#6f7376);clip-path:polygon(0 0,52% 0,52% 70%,100% 100%,0 100%)"></div>
</section>

</body>
</html>
```